Elegant, Premium looking Eye Lash Box/Case

We are a premium beauty brand and we are interested in creating a premium looking eye lash packaging.

I have attached the type of box we are after...

Box Measurements are:

Box board thickness 2mm
Length 110mm
Width 50mm
Height 20mm

Let me know if you require any further information.

Target Market(s)

Females 18-35

Industry/Entity Type

Cosmetics

Requirements
Must have
• Logo
• I have attached .jpg, let me know if you require in any other formats
Nice to have
• Linen pattern/brown colour for box/case
• Gold borderline around the top box
• Refer attached for photos

```html
<!DOCTYPE html>
<html lang="en">
<head>
<meta charset="utf-8">
<title>Lash Box Sleeve – Three Gold Line Variants</title>
<link rel="stylesheet" href="https://fonts.googleapis.com/css2?family=Cinzel:wght@500&display=swap">
<style>
  :root {
    --canvas-bg: #ffe6d8;
    --sleeve-brown: #3c1e0c;
    --sleeve-brown-soft: #45230f;
    --gold-light: #f3dc8e;
    --gold-mid: #c9a24a;
    --gold-deep: #8a6a26;
    --gold-text: #d9c08a;
  }
  * { box-sizing: border-box; margin: 0; padding: 0; }
  html, body { width: 1200px; height: 527px; overflow: hidden; }
  body { background: var(--canvas-bg); position: relative; }

  .sleeve {
    position: absolute;
    width: 169px;
    height: 282px;
    background: linear-gradient(160deg, var(--sleeve-brown-soft), var(--sleeve-brown));
  }
  .sleeve--one   { left: 101px; top: 126px; }
  .sleeve--two   { left: 450px; top: 127px; }
  .sleeve--three { left: 808px; top: 128px; }

  .brand-disc {
    position: absolute;
    width: 40px;
    height: 40px;
    border-radius: 50%;
    background: radial-gradient(circle at 40% 35%, var(--gold-light), var(--gold-mid) 55%, var(--gold-deep));
    transform: translate(-50%, -50%);
  }

  .brand-name {
    position: absolute;
    font-family: "Cinzel", serif;
    font-weight: 500;
    font-size: 9.5px;
    letter-spacing: 0.6px;
    color: var(--gold-text);
    white-space: nowrap;
    transform: translate(-50%, -50%) rotate(-90deg);
  }

  .gold-line {
    position: absolute;
    width: 2px;
    background: linear-gradient(180deg, var(--gold-deep), var(--gold-light) 45%, var(--gold-mid) 70%, var(--gold-deep));
  }
  .gold-line--thin { width: 1px; }
</style>
</head>
<body>

  <section class="sleeve sleeve--one" aria-label="Sleeve variant with a single long gold line">
    <span class="brand-disc" style="left:74px; top:142px;"></span>
    <span class="brand-name" style="left:110px; top:143px;">Marivelle Hart</span>
    <span class="gold-line" style="left:124px; top:35px; height:212px;"></span>
  </section>

  <section class="sleeve sleeve--two" aria-label="Sleeve variant with a double gold line">
    <span class="brand-disc" style="left:72px; top:142px;"></span>
    <span class="brand-name" style="left:109px; top:143px;">Marivelle Hart</span>
    <span class="gold-line gold-line--thin" style="left:121px; top:58px; height:176px;"></span>
    <span class="gold-line" style="left:126px; top:46px; height:197px;"></span>
  </section>

  <section class="sleeve sleeve--three" aria-label="Sleeve variant with a short gold line">
    <span class="brand-disc" style="left:74px; top:143px;"></span>
    <span class="brand-name" style="left:108px; top:143px;">Marivelle Hart</span>
    <span class="gold-line" style="left:121px; top:79px; height:131px;"></span>
  </section>

</body>
</html>
```